Corinne Dabney Interiors business cards

We need a DOUBLE SIDED business card design that is simple, elegant and modern. We are a rapidly growing Interior Design Firm, and our brand colours are blush pink, navy, and antique gold, so we require some or all of these colours to be used. The final design should portray elegance, simplicity, and have a modern feel. We have upload inspiration photos that have the feel we're looking for.

Industry/Entity Type

Interior Design

Contact Information for Business Card

Contact information and LOGO

Colors
EB3D1F
EC4F4E
F09395
F8D3D4
FCEDEE

Requirements
Must have
• Navy, the right shade of blush pink, and antique gold

```html
<!DOCTYPE html>
<html lang="en">
<head>
<meta charset="utf-8">
<title>Corinne Dabney Interiors – Business Cards</title>
<link rel="stylesheet" href="https://fonts.googleapis.com/css2?family=Jost:wght@400;500;600&display=swap">
<style>
  :root {
    --backdrop: #e4e3e3;
    --card: #fdeee2;
    --navy: #1f2a56;
    --gold: #a3845c;
    --ink: #1c1c24;
  }
  * { margin: 0; padding: 0; box-sizing: border-box; }
  html, body { width: 1126px; height: 1200px; overflow: hidden; }
  body {
    background: var(--backdrop);
    font-family: "Jost", sans-serif;
    position: relative;
  }

  .brand-lockup {
    position: absolute;
    left: 34px;
    top: 40px;
    display: flex;
    align-items: center;
    gap: 10px;
  }
  .brand-lockup .mark-square {
    width: 18px; height: 18px; background: var(--navy);
  }
  .brand-name {
    font-family: "Jost", sans-serif;
    font-weight: 400;
    color: var(--gold);
    text-transform: uppercase;
    letter-spacing: 0.02em;
  }
  .brand-lockup .brand-name { font-size: 15px; }

  .card {
    position: absolute;
    left: 243px;
    width: 640px;
    height: 364px;
    background: var(--card);
    overflow: hidden;
  }
  .card--front { top: 170px; }
  .card--back { top: 600px; }

  .band { position: absolute; }
  .band--navy { background: var(--navy); height: 22px; }
  .band--gold { background: var(--gold); height: 13px; }
  .band--top { top: 0; }
  .band--bottom { bottom: 0; }

  .card--front .brand-name {
    position: absolute;
    left: 0; right: 0;
    top: 168px;
    text-align: center;
    font-size: 22px;
  }

  .card--back .brand-name {
    position: absolute;
    left: 40px;
    width: 240px;
    top: 170px;
    text-align: center;
    font-size: 15px;
  }
  .divider {
    position: absolute;
    left: 320px;
    top: 76px;
    width: 1px;
    height: 212px;
    background: var(--navy);
  }
  .contact {
    position: absolute;
    left: 370px;
    top: 98px;
    color: var(--ink);
  }
  .contact__name {
    font-size: 22px;
    font-weight: 400;
    color: var(--gold);
    line-height: 1;
  }
  .contact__name strong { font-weight: 600; }
  .contact__title {
    font-size: 13px;
    font-weight: 500;
    margin-top: 4px;
    letter-spacing: 0.03em;
  }
  .contact__label {
    margin-top: 22px;
    font-size: 8px;
    font-weight: 600;
    color: var(--gold);
    letter-spacing: 0.06em;
    text-transform: uppercase;
  }
  .social {
    list-style: none;
    margin-top: 6px;
  }
  .social li {
    display: flex;
    align-items: center;
    gap: 8px;
    font-size: 11.5px;
    margin-bottom: 7px;
    letter-spacing: 0.02em;
  }
  .social .dot {
    width: 12px; height: 12px; border-radius: 50%;
    background: var(--gold);
    flex: none;
  }
  .details {
    margin-top: 14px;
    font-size: 11.5px;
    line-height: 1.3;
    letter-spacing: 0.03em;
  }
  .details .office { font-weight: 500; }
</style>
</head>
<body>

  <div class="brand-lockup">
    <span class="mark-square"></span>
    <span class="brand-name">Corinne Dabney Interiors</span>
  </div>

  <section class="card card--front" aria-label="Business card front">
    <span class="band band--gold band--top" style="left:188px;width:202px"></span>
    <span class="band band--navy band--top" style="left:390px;width:250px"></span>
    <p class="brand-name">Corinne Dabney Interiors</p>
    <span class="band band--navy band--bottom" style="left:0;width:250px"></span>
    <span class="band band--gold band--bottom" style="left:250px;width:200px"></span>
  </section>

  <section class="card card--back" aria-label="Business card back">
    <span class="band band--gold band--top" style="left:0;width:202px"></span>
    <span class="band band--navy band--top" style="left:202px;width:248px"></span>

    <p class="brand-name">Corinne Dabney Interiors</p>
    <span class="divider"></span>

    <div class="contact">
      <h1 class="contact__name">Corinne <strong>Dabney</strong></h1>
      <p class="contact__title">Principal Designer</p>
      <p class="contact__label">Find her on social</p>
      <ul class="social">
        <li><span class="dot"></span>corinnedabneyinteriors</li>
        <li><span class="dot"></span>corinne.dabney.interiors</li>
      </ul>
      <div class="details">
        <p class="office">Office # 905-555-0142</p>
        <p>corinne@cdinteriorsstudio.com</p>
        <p>www.corinnedabneyinteriors.com</p>
      </div>
    </div>

    <span class="band band--navy band--bottom" style="left:188px;width:249px"></span>
    <span class="band band--gold band--bottom" style="left:437px;width:203px"></span>
  </section>

</body>
</html>
```